Redesign Video/PIcture Check in Page

Redesign our current TetherWatchApp iPhone App checkin screens - Keep the design simple so that programmers do not have to do too much extra work to make your design work. - Look at the attached website screenshot for the overall look and feel, and color scheme - Convert the attached vector logo to iOS Icon format. - Deliver all graphics in the density required for iPhone XS Max. I will upload current check in pages that need to be reimagined. Check in needs to be more intutitive. Would like to add some gamification to the verification screen where they currently are required to enter series of random numbers. simple card game etc might work better. See TetherWatchapp in itunes and google play store. also visit quorvant-link.example or tetherwatchapp.example for more information about our company.
The Current Checkin Process:
A. Client receives alert to checkin or submits voluntary checkin
B. Clicks checkin button on home Screen.
Redesign from here:
C. Clicks on a check in from check in list screen(new screen)
D. Enters verification number(gamification something better than random numbers)
E. Opens Camera
D. Takes Selfie
F. submits photo
G. clicks check in
SEE CURRENT STEPS PIC I UPLOADED

Target Market(s)

Courts,Probation and parole,Attorneys,Sheriffs,Jails, Alternative sentencing

Colors
3277b5

Requirements
Must have
• Must be easy to navigate,Intuitive!
Nice to have
• Gamification of check in verification.
• Step by step process with next button or similar

```html
<!DOCTYPE html>
<html lang="en">
<head>
<meta charset="utf-8">
<title>TetherWatchApp – Check-In Screens</title>
<link href="https://fonts.googleapis.com/css2?family=Ubuntu:wght@400;500;700&family=Lato:wght@700;900&display=swap" rel="stylesheet">
<style>
:root{
  --page:#f4f4f5;
  --ink:#1d1d1f;
  --brand-blue:#3277b5;
  --brand-violet:#a47bb3;
  --body-top:#505b68;
  --body-bottom:#222b37;
  --pill:#ffffff;
  --pill-ink:#3a4250;
  --muted:#9aa0a8;
  --card-a:#3f6cb8;
  --card-b:#7462b3;
  --pending:#a5a8ae;
  --success:#8fd13a;
  --failed:#e2542a;
  --accent-red:#d2305a;
  --accent-plum:#b3306a;
}
*{box-sizing:border-box;margin:0;padding:0}
html,body{width:1200px;height:1200px;overflow:hidden}
body{background:var(--page);font-family:"Ubuntu",sans-serif;color:var(--ink);position:relative}
.section-title{position:absolute;top:192px;font-size:35px;font-weight:500;letter-spacing:.2px}
.screen{position:absolute;top:242px;width:331px;height:718px;overflow:hidden;
  background:linear-gradient(180deg,var(--body-top),var(--body-bottom))}
.screen>*{position:absolute}
.app-bar{left:0;top:0;width:100%;height:44px;background:linear-gradient(90deg,var(--brand-blue) 40%,var(--brand-violet));
  color:#fff;font-size:20px;font-weight:500;display:flex;align-items:center;justify-content:center;z-index:3}
.app-foot{left:0;bottom:0;width:100%;height:44px;background:linear-gradient(90deg,var(--brand-blue) 40%,var(--brand-violet));z-index:3}
.home-indicator{left:106px;bottom:8px;width:120px;height:4px;border-radius:2px;background:#fff;z-index:4}
.pill{background:var(--pill);border-radius:14px;color:var(--pill-ink);font-size:13.5px;display:flex;align-items:center;justify-content:center;gap:4px;height:27px;top:54px;box-shadow:0 2px 4px rgba(0,0,0,.25)}
.pill.nav{font-size:14.5px}
.pill .menu{width:11px;height:9px;border-top:2px solid currentColor;border-bottom:2px solid currentColor;position:relative}
.pill .menu::after{content:"";position:absolute;left:0;right:0;top:1.5px;border-top:2px solid currentColor}
.pill.right{left:249px;width:76px;font-size:11.5px}
/* home */
.battery{left:6px;top:92px;width:77px;height:27px;border-radius:14px;background:#fff;display:flex;align-items:center;justify-content:center;gap:5px;font:700 8px "Lato",sans-serif;color:#333}
.battery .cell{width:30px;height:13px;border:1.5px solid #555;border-radius:2px;background:linear-gradient(#6bd24a,#3da62b);position:relative}
.battery .cell::after{content:"";position:absolute;right:-4px;top:3px;width:2px;height:5px;background:#555}
.battery-label{left:6px;top:121px;width:77px;text-align:center;font:700 7.5px "Lato",sans-serif;color:#fff}
.avatar-ring{left:83px;top:87px;width:166px;height:166px;border-radius:50%;background:#8d939b}
.avatar{left:98px;top:102px;width:136px;height:136px;border-radius:50%;background:radial-gradient(circle at 50% 45%,#5b4a44,#2b2f4a 70%,#1f2850)}
.user-name{left:0;width:100%;top:256px;text-align:center;color:#fff;font-size:20px}
.tile{width:108px;height:108px;border-radius:50%;background:#fff;display:flex;align-items:center;justify-content:center;box-shadow:0 2px 6px rgba(0,0,0,.3)}
.tile.sm{width:80px;height:80px}
.tile-label{width:160px;text-align:center;color:#fff;font-size:24px;font-weight:500}
.tile-label.sm{font-size:17px}
/* check-in */
.stamp{left:7px;top:108px;width:317px;height:30px;border-radius:15px;background:#fff;display:flex;color:#4a4f57;font-size:16px;font-weight:500}
.stamp span{flex:1;display:flex;align-items:center;justify-content:center}
.stamp span+span{border-left:1px solid #c9ccd1}
.banner{left:6px;top:151px;width:319px;height:43px;border-radius:22px;background:linear-gradient(90deg,#2f6fb3,#8a6ab4);color:#fff;font-size:23px;display:flex;align-items:center;justify-content:center;box-shadow:0 2px 4px rgba(0,0,0,.3)}
.label{color:#fff;font-size:15px;font-weight:700}
.code{left:106px;top:230px;width:110px;height:40px;border-radius:20px;background:#fff;color:#3a3f47;font-size:29px;font-weight:700;display:flex;align-items:center;justify-content:center}
.field{left:15px;width:303px;height:43px;border-radius:14px;background:#fff;color:var(--muted);font-size:18.5px;padding-left:15px;display:flex;align-items:center}
.selfie-frame{left:97px;top:442px;width:137px;height:137px}
.submit{left:138px;top:590px;width:56px;height:56px;border-radius:50%;background:#fff;display:flex;align-items:center;justify-content:center}
.submit-label{left:0;width:100%;top:649px;text-align:center;color:#fff;font-size:11.5px;font-weight:500}
/* history */
.card{left:6px;width:319px;height:70px;border-radius:18px;background:linear-gradient(90deg,var(--card-a),var(--card-b));color:#fff;box-shadow:0 2px 4px rgba(0,0,0,.3)}
.card .meta{position:absolute;left:16px;top:11px;font-size:13.5px;font-weight:500;color:#e3e6f3;display:flex;gap:9px}
.card .meta i{width:1px;height:16px;background:#b5bde0}
.card .title{position:absolute;left:16px;top:32px;font-size:23px;white-space:nowrap}
.badge{position:absolute;left:226px;top:10px;width:77px;height:19px;border-radius:10px;font-size:11px;font-weight:500;display:flex;align-items:center;justify-content:center;color:#fff}
.badge.pending{background:var(--pending);color:#3a3d44}
.badge.success{background:linear-gradient(90deg,#a6db41,var(--success));color:#1f3d08}
.badge.failed{background:linear-gradient(90deg,#f07a2b,var(--failed))}
</style>
</head>
<body>

<h2 class="section-title" style="left:51px">1. Home</h2>
<h2 class="section-title" style="left:437px">2. Check-In</h2>
<h2 class="section-title" style="left:819px">3. Check-In History</h2>

<!-- Home -->
<section class="screen" style="left:51px">
  <div class="app-bar">TetherWatchApp</div>
  <div class="pill nav" style="left:6px;width:77px"><span class="menu"></span>HOME</div>
  <div class="pill right">SIGN OUT</div>
  <div class="battery"><span class="cell"></span>100%</div>
  <div class="battery-label">My Bracelet</div>
  <div class="avatar-ring"></div>
  <div class="avatar" role="img" aria-label="Profile photo of the client"></div>
  <div class="user-name">Marcus T Bellamy</div>

  <div class="tile" style="left:36px;top:302px">
    <svg width="70" height="70" viewBox="0 0 70 70">
      <g fill="none" stroke="#2a3340" stroke-width="4" stroke-linecap="round">
        <path d="M36 14a16 16 0 0 1 16 16"/><path d="M36 22a8 8 0 0 1 8 8"/>
      </g>
      <circle cx="36" cy="30" r="3" fill="#2a3340"/>
      <path d="M36 30L30 42" stroke="#2a3340" stroke-width="3"/>
      <ellipse cx="32" cy="50" rx="26" ry="9" fill="#3d72a8" stroke="#2a3340" stroke-width="3"/>
      <ellipse cx="32" cy="46" rx="22" ry="6" fill="#fff" stroke="#2a3340" stroke-width="2"/>
    </svg>
  </div>
  <div class="tile-label" style="left:10px;top:410px">BRACELET</div>

  <div class="tile" style="left:192px;top:302px">
    <svg width="74" height="60" viewBox="0 0 74 60"><path d="M6 30l20 20L68 8" fill="none" stroke="#6fc52e" stroke-width="11" stroke-linecap="round" stroke-linejoin="round"/></svg>
  </div>
  <div class="tile-label" style="left:166px;top:410px">CHECK IN</div>

  <div class="tile sm" style="left:50px;top:452px">
    <svg width="72" height="72" viewBox="0 0 72 72">
      <circle cx="36" cy="36" r="35" fill="#6a6aae"/>
      <path d="M20 24c0-6 4-10 9-10s9 4 9 10c0 7-9 16-9 16s-9-9-9-16z" fill="#fff"/>
      <circle cx="29" cy="24" r="3.5" fill="#6a6aae"/>
    </svg>
  </div>
  <div class="tile-label sm" style="left:10px;top:532px">MAPS</div>

  <div class="tile sm" style="left:206px;top:452px">
    <svg width="50" height="44" viewBox="0 0 50 44">
      <rect x="2" y="14" width="8" height="30" fill="#e8542a"/><rect x="14" y="2" width="8" height="42" fill="#f08a2a"/>
      <rect x="26" y="18" width="8" height="26" fill="#e8542a"/><rect x="38" y="10" width="8" height="34" fill="#f08a2a"/>
    </svg>
  </div>
  <div class="tile-label sm" style="left:166px;top:532px">MY STATS</div>

  <div class="tile sm" style="left:50px;top:560px">
    <svg width="44" height="48" viewBox="0 0 44 48">
      <circle cx="22" cy="13" r="11" fill="var(--accent-red)"/>
      <path d="M2 46c0-12 9-20 20-20s20 8 20 20z" fill="var(--accent-plum)"/>
    </svg>
  </div>
  <div class="tile-label sm" style="left:10px;top:638px">PROFILE</div>

  <div class="tile sm" style="left:206px;top:560px">
    <svg width="40" height="56" viewBox="0 0 40 56">
      <circle cx="22" cy="6" r="5" fill="#8a5fb5"/>
      <path d="M12 22l10-4-8 28c4 0 9-3 12-6" fill="none" stroke="#7a55ad" stroke-width="6" stroke-linecap="round" stroke-linejoin="round"/>
    </svg>
  </div>
  <div class="tile-label sm" style="left:166px;top:638px">INFORMATION</div>

  <div class="app-foot"></div>
  <div class="home-indicator"></div>
</section>

<!-- Check-In -->
<section class="screen" style="left:434px">
  <div class="app-bar">TetherWatchApp</div>
  <div class="pill nav" style="left:6px;width:96px"><span class="menu"></span>CHECK IN</div>
  <div class="pill right">CANCEL</div>
  <div class="stamp"><span>30 Oct 2018</span><span>14:50:23</span></div>
  <div class="banner">Voluntary Check-In Request</div>
  <div class="label" style="left:14px;top:205px">Please Check-In and Quote this number:</div>
  <div class="code">C96M</div>
  <div class="field" style="top:285px">Type the above code</div>
  <div class="label" style="left:14px;top:337px">Comment:</div>
  <div class="field" style="top:359px">Type to reply</div>
  <div class="label" style="left:14px;top:411px">Take your Selfie:</div>
  <svg class="selfie-frame" viewBox="0 0 137 137">
    <g fill="none" stroke="#fff" stroke-width="3">
      <path d="M2 30V2h34"/><path d="M101 2h34v28"/><path d="M135 107v28h-34"/><path d="M36 135H2v-28"/>
    </g>
    <rect x="10" y="10" width="117" height="116" fill="#fff"/>
    <circle cx="68" cy="45" r="21" fill="var(--accent-red)"/>
    <path d="M28 113c0-26 18-40 40-40s40 14 40 40z" fill="var(--accent-plum)"/>
  </svg>
  <div class="submit"><svg width="34" height="26" viewBox="0 0 34 26"><path d="M3 13l10 10L31 3" fill="none" stroke="#4b68b0" stroke-width="5" stroke-linecap="round" stroke-linejoin="round"/></svg></div>
  <div class="submit-label">CHECK IN</div>
  <div class="app-foot"></div>
  <div class="home-indicator"></div>
</section>

<!-- Check-In History -->
<section class="screen" style="left:818px">
  <div class="app-bar">TetherWatchApp</div>
  <div class="pill nav" style="left:6px;width:160px"><span class="menu"></span>CHECK IN HISTORY</div>
  <div class="pill right">REFRESH</div>

  <div class="card" style="top:106px"><div class="meta">30 Oct 2018<i></i>14:50:23</div><div class="badge pending">PENDING</div><div class="title">Voluntary Check-In Request</div></div>
  <div class="card" style="top:186px"><div class="meta">29 Oct 2018<i></i>16:49:54</div><div class="badge success">SUCCESS</div><div class="title">Voluntary Check-In Request</div></div>
  <div class="card" style="top:265px"><div class="meta">29 Oct 2018<i></i>16:49:54</div><div class="badge failed">FAILED</div><div class="title">Voluntary Check-In Request</div></div>
  <div class="card" style="top:345px"><div class="meta">27 Oct 2018<i></i>10:51:39</div><div class="badge success">SUCCESS</div><div class="title">Voluntary Check-In Request</div></div>
  <div class="card" style="top:424px"><div class="meta">27 Oct 2018<i></i>10:49:27</div><div class="badge success">SUCCESS</div><div class="title">Voluntary Check-In Request</div></div>
  <div class="card" style="top:504px"><div class="meta">26 Oct 2018<i></i>17:59:50</div><div class="badge success">SUCCESS</div><div class="title">Voluntary Check-In Request</div></div>
  <div class="card" style="top:583px"><div class="meta">26 Oct 2018<i></i>17:58:44</div><div class="badge success">SUCCESS</div><div class="title">Voluntary Check-In Request</div></div>
  <div class="card" style="top:663px"><div class="badge success"></div></div>

  <div class="app-foot"></div>
</section>

</body>
</html>
```